Health and Fitness Club requires membership pack

We need a membership pack, like this style (http://www.pamphletcraftonline.co.uk/images/A4_pocket_folder_round.jpg) a4 sized.

The front of it should contain our logo, the entire thing should be in the style of our brand/concept. On the inside left side there should be space for copy which we will provide once the design has been selected (approximately 500 words).

At the bottom of the left page inside, should be the following:
telephone icon | bbm icon
instagram logo | twitter logo | kik logo | email logo

with the relevant contact details for our company, underneath this should be our website written so that it occupies the entire width of the page.

our website is www. v i g o r b a s e . ae and our logo is attached

i have included a flyer we recently produced to give you an idea of the creative direction of the brand..

```html
<!DOCTYPE html>
<html lang="en">
<head>
<meta charset="utf-8">
<title>Vigor Base – Membership Pack</title>
<link href="https://fonts.googleapis.com/css2?family=Oswald:wght@700&family=Open+Sans:wght@400;600&family=Source+Serif+4:wght@400&display=swap" rel="stylesheet">
<style>
  :root {
    --page: #ffffff;
    --ink: #111111;
    --panel: #000000;
    --panel-soft: #1c1c1c;
    --red: #c0111f;
    --white: #ffffff;
    --body-grey: #b9b9b9;
    --fold: #9a9a9a;
  }
  * { box-sizing: border-box; margin: 0; padding: 0; }
  html, body { width: 807px; height: 1200px; overflow: hidden; background: var(--page); }
  body { position: relative; font-family: "Open Sans", Arial, sans-serif; }

  .spread-label {
    position: absolute;
    font-family: "Source Serif 4", Georgia, serif;
    font-size: 19px;
    color: var(--ink);
  }

  .spread {
    position: absolute;
    overflow: hidden;
    box-shadow: 0 2px 3px rgba(0,0,0,.35);
  }
  .spread--outside { left: 24px; top: 59px; width: 764px; height: 525px; background: var(--panel); }
  .spread--inside { left: 31px; top: 637px; width: 748px; height: 522px; background: var(--panel); }

  .fold {
    position: absolute; top: 0; bottom: 0; width: 0;
    border-left: 1px dashed var(--fold);
    z-index: 3;
  }
  .spread--outside .fold { left: 382px; }
  .spread--inside .fold { left: 374px; }

  .backdrop { position: absolute; inset: 0; }

  /* brand name in place of the mark */
  .brand-seal {
    position: absolute;
    display: flex; align-items: center; justify-content: center;
    border-radius: 50%;
    border: 2px solid var(--white);
    background: var(--panel);
  }
  .brand-seal__name {
    font-family: "Oswald", Impact, sans-serif;
    font-weight: 700;
    color: var(--white);
    text-transform: uppercase;
    text-align: center;
    line-height: 1;
  }

  .back-cover__seal { left: 160px; top: 385px; width: 60px; height: 60px; }
  .back-cover__seal .brand-seal__name { font-size: 11px; }

  .contact-row { position: absolute; left: 0; top: 471px; width: 382px; height: 14px; }
  .contact {
    position: absolute; top: 0;
    display: flex; align-items: center; gap: 3px;
    font-size: 6.5px; font-weight: 600; color: var(--white);
    white-space: nowrap;
  }
  .contact__dot { width: 10px; height: 10px; border-radius: 50%; background: var(--red); flex: none; }
  .contact__icon { width: 11px; height: 11px; flex: none; }

  .web-address {
    position: absolute; left: 24px; top: 492px; width: 338px;
    display: flex; justify-content: space-between;
    font-size: 8.5px; font-weight: 600; color: var(--red);
  }

  .cover__watermark {
    position: absolute; left: 420px; top: 55px; width: 260px; height: 260px;
    border-radius: 50%; background: #2a2a2a; opacity: .55;
  }
  .cover__seal { left: 471px; top: 126px; width: 160px; height: 160px; border-width: 4px; }
  .cover__seal .brand-seal__name { font-size: 30px; }

  .wordmark {
    position: absolute;
    font-family: "Oswald", Impact, sans-serif;
    font-weight: 700;
    text-transform: uppercase;
    color: var(--red);
    line-height: .92;
    text-align: right;
  }
  .cover__wordmark { left: 500px; top: 372px; width: 182px; font-size: 58px; }

  .inside__wordmark { left: 56px; top: 82px; width: 170px; font-size: 56px; text-align: left; }

  .member-copy {
    position: absolute; left: 73px; top: 220px; width: 254px;
    font-size: 6.6px; line-height: 9.6px; color: var(--body-grey);
  }
  .member-copy p { margin-bottom: 9px; }

  .pocket { position: absolute; left: 0; top: 0; }
  .pocket__seal { left: 612px; top: 360px; width: 100px; height: 100px; border-width: 3px; }
  .pocket__seal .brand-seal__name { font-size: 18px; }
</style>
</head>
<body>

  <span class="spread-label" style="left:32px;top:10px;">back cover</span>
  <span class="spread-label" style="left:420px;top:10px;">cover</span>

  <section class="spread spread--outside">
    <svg class="backdrop" width="764" height="525" viewBox="0 0 764 525" aria-hidden="true">
      <defs>
        <radialGradient id="glow" cx="0.32" cy="0.12" r="0.6">
          <stop offset="0" stop-color="#3a3a3a"/>
          <stop offset="1" stop-color="#0c0c0c"/>
        </radialGradient>
        <radialGradient id="glow-right" cx="0.5" cy="0.2" r="0.6">
          <stop offset="0" stop-color="#2c2c2c"/>
          <stop offset="1" stop-color="#0a0a0a"/>
        </radialGradient>
      </defs>
      <rect x="0" y="0" width="382" height="525" fill="url(#glow)"/>
      <rect x="382" y="0" width="382" height="525" fill="url(#glow-right)"/>
      <path d="M0 150 C120 60 260 40 382 70" fill="none" stroke="#444" stroke-width="26" opacity=".35"/>
      <path d="M0 260 C140 170 250 120 382 130" fill="none" stroke="#3a3a3a" stroke-width="18" opacity=".3"/>
      <path d="M0 360 C160 250 280 220 382 230" fill="none" stroke="#333" stroke-width="10" opacity=".25"/>
      <path d="M382 60 C520 20 660 20 764 70" fill="none" stroke="#3a3a3a" stroke-width="22" opacity=".3"/>
    </svg>

    <div class="brand-seal back-cover__seal"><span class="brand-seal__name">Vigor<br>Base</span></div>

    <div class="contact-row">
      <span class="contact" style="left:24px;"><span class="contact__dot"></span>@vigorbase.ae</span>
      <span class="contact" style="left:107px;"><span class="contact__dot"></span>@vigorbase.ae</span>
      <span class="contact" style="left:187px;"><span class="contact__dot"></span>@vigorbase.ae</span>
      <span class="contact" style="left:278px;">
        <svg class="contact__icon" viewBox="0 0 11 11" aria-hidden="true">
          <circle cx="5.5" cy="5.5" r="5.5" fill="var(--red)"/>
          <rect x="2.5" y="3.5" width="6" height="4" fill="none" stroke="#fff" stroke-width=".8"/>
          <path d="M2.5 3.5 L5.5 6 L8.5 3.5" fill="none" stroke="#fff" stroke-width=".8"/>
        </svg>info@vigorbase.ae</span>
    </div>

    <div class="web-address" aria-label="www.vigorbase.ae">
      <span>w</span><span>w</span><span>w</span><span>.</span><span>v</span><span>i</span><span>g</span><span>o</span><span>r</span><span>b</span><span>a</span><span>s</span><span>e</span><span>.</span><span>a</span><span>e</span>
    </div>

    <div class="cover__watermark" role="img" aria-label="Faint enlarged brand emblem behind the cover seal"></div>
    <div class="brand-seal cover__seal"><span class="brand-seal__name">Vigor<br>Base</span></div>
    <div class="wordmark cover__wordmark">Vigor<br>Base</div>

    <div class="fold"></div>
  </section>

  <span class="spread-label" style="left:32px;top:612px;">inside</span>

  <section class="spread spread--inside">
    <div class="wordmark inside__wordmark">Vigor<br>Base</div>

    <div class="member-copy">
      <p>Welcome to Vigor Base, the club built for people who train with purpose. This pack holds everything you need to begin your membership, from class times and coaching options to the house rules that keep our floor safe, clean and focused for every member who walks through the door.</p>
      <p>Our coaches will meet you in your first week to set clear goals and build a plan that fits your schedule.</p>
      <p>Strength, conditioning and recovery sit at the heart of everything we do. Book sessions at the front desk or through our members line, and ask any coach for help with form, load or progress. Ready to start?</p>
      <p>Lockers, towels and water are included with every plan. Please bring a lock, wear clean training shoes and wipe down kit after use. Opening hours, holiday times and class updates are shared each week on our social pages.</p>
    </div>

    <svg class="pocket" width="748" height="522" viewBox="0 0 748 522" aria-hidden="true">
      <path d="M388 522 C450 400 580 330 748 317 L748 522 Z" fill="var(--red)"/>
    </svg>
    <div class="brand-seal pocket__seal"><span class="brand-seal__name">Vigor<br>Base</span></div>

    <div class="fold"></div>
  </section>

</body>
</html>
```